Jazz: Journey Through the Harlem Renaissance and the Black Arts Movement

Corvel Tavern invites you on a musical Journey Through the Harlem Renaissance and the Black Arts Movement!
Join us for an afternoon of Jazz on Sunday, February 27, 2022 from 3pm – 5pm.
Local jazz artists will thrill you with the music of legendary Harlem Renaissance artists such as Royce Tamberlin and Odessa Crane and famed Black Arts Movement stylings reminiscent of Vernon Askew and Lydia Farrow.
There will be games, prizes and opportunities to support arts programs at local schools.

```html
<!DOCTYPE html>
<html lang="en">
<head>
<meta charset="utf-8">
<title>Corvel Tavern – Jazz Afternoon</title>
<link rel="stylesheet" href="https://fonts.googleapis.com/css2?family=Bebas+Neue&family=Playfair+Display:wght@700&family=Roboto:wght@700&family=Roboto+Slab:wght@300;400;700&display=swap">
<style>
  :root {
    --orange: #fba93f;
    --ink: #1e1d22;
    --red: #c93b24;
    --gold: #d9a232;
    --white: #ffffff;
    --rule: #5a5960;
  }
  * { box-sizing: border-box; margin: 0; padding: 0; }
  html, body { width: 900px; height: 1200px; overflow: hidden; background: var(--white); }
  .canvas { position: relative; width: 900px; height: 1200px; overflow: hidden; }
  .poster { position: absolute; left: 90px; top: 91px; width: 720px; height: 1018px; background: var(--orange); }
  .panel {
    position: absolute; left: 30px; top: 27px; width: 665px; height: 959px;
    background: var(--ink); border-radius: 54px 54px 30px 30px;
  }
  .layer { position: absolute; left: 0; top: 0; width: 900px; height: 1200px; }
  .venue-title {
    position: absolute; left: 0; width: 900px; top: 141px; text-align: center;
    font-family: "Bebas Neue", "Arial Narrow", sans-serif; font-weight: 400; font-size: 78px; line-height: 1;
    letter-spacing: 0.17em; text-indent: 0.17em; color: var(--gold);
  }
  .rule { position: absolute; left: 216px; width: 468px; height: 1px; background: var(--rule); }
  .rule.top { top: 223px; }
  .rule.bottom { top: 263px; }
  .invite {
    position: absolute; left: 0; width: 900px; top: 228px; text-align: center;
    font-family: "Roboto Slab", Georgia, serif; font-weight: 300; font-size: 28px; line-height: 32px;
    letter-spacing: 0.5em; text-indent: 0.5em; color: var(--white);
  }
  .lead {
    position: absolute; left: 0; width: 900px; top: 272px; text-align: center;
    font-family: "Roboto Slab", Georgia, serif; font-size: 19px; line-height: 22px; color: var(--white);
  }
  .movement-banner { position: absolute; top: 304px; left: 156px; height: 49px; display: flex; }
  .movement-banner .part { height: 49px; overflow: hidden; white-space: nowrap; }
  .movement-banner .harlem { background: var(--red); color: var(--white); width: 271px; border-radius: 4px 0 0 4px; padding-left: 15px; }
  .movement-banner .black-arts { background: var(--orange); color: var(--ink); width: 317px; border-radius: 0 4px 4px 0; padding-left: 14px; }
  .movement-banner .fit {
    display: inline-block; transform-origin: left center;
    font-family: "Bebas Neue", "Arial Narrow", sans-serif; font-weight: 400;
    font-size: 40px; line-height: 51px;
  }
  .movement-banner .harlem .fit { transform: scaleX(0.86); }
  .movement-banner .black-arts .fit { transform: scaleX(0.84); }
  .join {
    position: absolute; left: 0; width: 900px; top: 372px; text-align: center;
    font-family: "Playfair Display", Georgia, serif; font-weight: 700; font-size: 19px; line-height: 24px; color: var(--white);
  }
  .date-pill {
    position: absolute; left: 186px; top: 403px; width: 527px; height: 36px;
    background: var(--red); border-radius: 18px; display: flex; align-items: center;
    font-family: "Roboto", Arial, sans-serif; font-weight: 700; font-size: 24px;
  }
  .date-pill .date { width: 345px; text-align: center; color: var(--white); white-space: nowrap; }
  .date-pill .time {
    position: absolute; right: 0; top: 0; width: 182px; height: 36px; line-height: 32px;
    background: var(--orange); border: 2px solid var(--red); border-radius: 18px;
    text-align: center; color: var(--ink); white-space: nowrap;
  }
  .description {
    position: absolute; left: 165px; top: 905px; width: 340px; white-space: nowrap;
    font-family: "Roboto Slab", Georgia, serif; font-size: 13.6px; line-height: 17.7px; color: var(--white);
  }
  .description strong { color: var(--orange); font-weight: 700; }
  .perks {
    position: absolute; left: 165px; top: 1003px; width: 360px; white-space: nowrap;
    font-family: "Roboto Slab", Georgia, serif; font-weight: 700; font-size: 15.5px; line-height: 19px; color: var(--white);
  }
  .venue-mark {
    position: absolute; left: 540px; top: 900px; width: 200px; text-align: center;
    font-family: "Roboto Slab", Georgia, serif; font-weight: 700; font-size: 30px; line-height: 34px; color: var(--gold);
  }
  .venue-mark .dot { display: block; width: 14px; height: 14px; margin: 0 auto 10px; border-radius: 50%; background: var(--gold); }
</style>
</head>
<body>
<div class="canvas">
  <div class="poster"><div class="panel"></div></div>

  <svg class="layer" width="900" height="1200" viewBox="0 0 900 1200">
    <defs>
      <linearGradient id="sunTone" x1="0" y1="0" x2="0.6" y2="1">
        <stop offset="0" stop-color="#fba93f"/>
        <stop offset="1" stop-color="#e2702e"/>
      </linearGradient>
    </defs>
    <g class="staff-lines" fill="#fba93f">
      <rect x="120" y="570" width="665" height="6"/>
      <rect x="120" y="621" width="665" height="6"/>
      <rect x="120" y="672" width="665" height="6"/>
      <rect x="120" y="723" width="665" height="6"/>
      <rect x="120" y="774" width="665" height="6"/>
    </g>
    <circle class="sax-illustration" cx="450" cy="672" r="190" fill="url(#sunTone)"
      role="img" aria-label="Illustration of a red saxophone in front of an orange sun with musical notes and sharps"/>
  </svg>

  <h1 class="venue-title">Corvel Tavern</h1>
  <div class="rule top"></div>
  <p class="invite">INVITES YOU</p>
  <div class="rule bottom"></div>
  <p class="lead">on a musical journey through the</p>

  <div class="movement-banner">
    <div class="part harlem"><span class="fit">HARLEM RENAISSANCE &amp;</span></div>
    <div class="part black-arts"><span class="fit">THE BLACK ARTS MOVEMENT!</span></div>
  </div>

  <p class="join">JOIN US FOR AN AFTERNOON OF JAZZ ON</p>
  <div class="date-pill">
    <span class="date">Sunday, February 27, 2022</span>
    <span class="time">3pm – 5pm</span>
  </div>

  <p class="description">Local jazz artists will thrill you with the music<br>of <strong>legendary Harlem Renaissance</strong> artists such as<br><strong>Royce Tamberlin</strong> and <strong>Odessa Crane</strong> and famed <strong>Black</strong><br><strong>Arts Movement</strong> stylings reminiscent of<br>Vernon Askew and Lydia Farrow.</p>
  <p class="perks">There will be games, prizes and opportunities<br>to support arts programs at local schools.</p>

  <div class="venue-mark"><span class="dot"></span>Corvel<br>Tavern</div>
</div>
</body>
</html>
```